Clinique VeraNova business card

I am looking for a talented designer who can an existing design and make it better. I need a 2 sided business card to represent our Psychology clinic staff members. It would need to be elegant, yet modern, clean, light and uplifting. Simple design, quick turnaround time. Lots of files and logos to use as your guide. I hope to hear from you!

Target Market(s)

Clients who receive the card of our therapists

Industry/Entity Type

Health And Wellness

Contact Information for Business Card

Following the similar designs of the Maplebrook Care Center card, there will be 2 sides. Side 1 (front) should have the veranova logo instead of the maplebrook care logo, The title should read Clinique VeraNova instead of centre Bien-Être Mésange/Maplebrook care Center.

Side 2 should have a spiral similar to the one on the card with sunflower leaves, and the title of the Therapist should be Marielle Odile Brunet, Psychologue, Psychologist, her email: Marielle@Veranova-example.com and phone number should be (514) 555-0137

Font styles to use
Serif

Colors
fee18a
85cae6
ffffff
0255a3

Requirements
Must have
• Side 1 (front): veranova logo- Name of the clinic, clinic address, contact info of clinic etc. use little icons in front of each (just like on sample card)
side 2: Therapist name titles and their contact info underneath with design of spiral and/or sunflower leaves..
Nice to have
• soft colors along soft yellow/gold and blue like the logo,
mini icons for phone, email, address etc.
We do work with a holistic, zen approach so it should represent that to some extent

```html
<!DOCTYPE html>
<html lang="fr">
<head>
<meta charset="utf-8">
<title>Clinique VeraNova – cartes professionnelles</title>
<link rel="stylesheet" href="https://fonts.googleapis.com/css2?family=Libre+Baskerville:wght@400;700&display=swap">
<style>
  :root {
    --ink: #221c6c;
    --sun: #e9dc14;
    --sun-soft: #f4ea6a;
    --paper: #ffffff;
    --backdrop: #eeeeec;
    --card-shadow: rgba(40, 30, 10, 0.14);
  }
  * { box-sizing: border-box; margin: 0; padding: 0; }
  html, body {
    width: 1200px; height: 800px; overflow: hidden;
    background: var(--backdrop);
    font-family: "Libre Baskerville", "Times New Roman", serif;
    color: var(--ink);
  }
  .sheet { position: relative; width: 1200px; height: 800px; }
  .card {
    position: absolute;
    width: 520px; height: 297px;
    background: var(--paper);
    box-shadow: 0 10px 30px var(--card-shadow);
    overflow: hidden;
  }
  .card--front { left: 50px; top: 251px; }
  .card--back { left: 630px; top: 251px; }

  /* Front */
  .brand {
    position: absolute; left: 0; right: 0; top: 52px;
    display: flex; justify-content: center; align-items: center; gap: 12px;
  }
  .brand__dot { width: 22px; height: 22px; border-radius: 50%; background: var(--sun); }
  .brand__name { font-size: 34px; font-weight: 400; color: var(--ink); letter-spacing: 0.5px; }
  .clinic-title {
    position: absolute; left: 0; right: 0; top: 128px;
    text-align: center; font-size: 29px; font-weight: 400;
  }
  .contact-grid {
    position: absolute; left: 20px; right: 20px; top: 182px;
    display: grid; grid-template-columns: 1fr 1fr; column-gap: 16px; row-gap: 8px;
    font-size: 11.5px;
  }
  .contact { display: flex; align-items: center; gap: 7px; }
  .contact--left { justify-content: flex-end; }
  .contact--wide { grid-column: 1 / -1; justify-content: center; font-size: 13px; margin-top: 6px; }
  .icon { width: 12px; height: 12px; flex: none; }

  /* Back */
  .petal-field {
    position: absolute; left: -70px; top: 70px;
    width: 360px; height: 360px; border-radius: 50%;
    background: radial-gradient(circle, var(--ink) 0 28%, var(--paper) 29% 35%, var(--sun) 36% 70%, var(--sun-soft) 71% 100%);
  }
  .therapist {
    position: absolute; right: 28px; top: 46px; width: 300px;
    text-align: center;
  }
  .therapist__name { font-size: 24px; font-weight: 400; line-height: 1.15; }
  .therapist__role { font-size: 13px; margin-top: 4px; }
  .therapist__icons { display: flex; justify-content: center; gap: 10px; margin-top: 16px; }
  .therapist__contact { font-size: 11.5px; line-height: 1.7; margin-top: 6px; }
</style>
</head>
<body>
<main class="sheet">

  <section class="card card--front" aria-label="Recto">
    <div class="brand">
      <span class="brand__dot"></span>
      <span class="brand__name">VeraNova</span>
    </div>
    <h1 class="clinic-title">Clinique VeraNova</h1>
    <div class="contact-grid">
      <p class="contact contact--left">514-555-0137
        <svg class="icon" viewBox="0 0 12 12"><circle cx="6" cy="6" r="5.5" fill="none" stroke="currentColor"/><path d="M4 3.2l1 1.2-.6.8c.5 1 1.2 1.7 2.2 2.2l.8-.6 1.2 1-.7 1c-2.3-.4-4.1-2.2-4.5-4.5z" fill="currentColor"/></svg>
      </p>
      <p class="contact">
        <svg class="icon" viewBox="0 0 12 12"><circle cx="6" cy="6" r="5.5" fill="none" stroke="currentColor"/><rect x="3" y="4" width="6" height="4.2" fill="none" stroke="currentColor" stroke-width=".8"/><path d="M3 4l3 2.3L9 4" fill="none" stroke="currentColor" stroke-width=".8"/></svg>
        info@veranova-example.com</p>
      <p class="contact contact--left">www.veranova-example.com
        <svg class="icon" viewBox="0 0 12 12"><circle cx="6" cy="6" r="5.5" fill="none" stroke="currentColor"/><circle cx="6" cy="6" r="2.8" fill="none" stroke="currentColor" stroke-width=".8"/><path d="M3.2 6h5.6M6 3.2v5.6" stroke="currentColor" stroke-width=".6"/></svg>
      </p>
      <p class="contact">
        <svg class="icon" viewBox="0 0 12 12"><circle cx="6" cy="6" r="5.5" fill="none" stroke="currentColor"/><circle cx="6" cy="6" r="2" fill="currentColor"/></svg>
        veranova-example.com/social</p>
      <p class="contact contact--wide">
        <svg class="icon" viewBox="0 0 12 12"><path d="M6 11s-3.5-4-3.5-6.3a3.5 3.5 0 0 1 7 0C9.5 7 6 11 6 11z" fill="currentColor"/><circle cx="6" cy="4.7" r="1.2" fill="var(--paper)"/></svg>
        4820 boul. des Érables ouest, Laval, Qc., H7X 2K4</p>
    </div>
  </section>

  <section class="card card--back" aria-label="Verso">
    <div class="petal-field" role="img" aria-label="Motif décoratif : spirale bleue entourée de pétales de tournesol jaunes"></div>
    <div class="therapist">
      <h2 class="therapist__name">Marielle Odile Brunet</h2>
      <p class="therapist__role">Psychologue, Psychologist</p>
      <div class="therapist__icons">
        <svg class="icon" viewBox="0 0 12 12"><circle cx="6" cy="6" r="5.5" fill="none" stroke="currentColor"/><path d="M4 3.2l1 1.2-.6.8c.5 1 1.2 1.7 2.2 2.2l.8-.6 1.2 1-.7 1c-2.3-.4-4.1-2.2-4.5-4.5z" fill="currentColor"/></svg>
        <svg class="icon" viewBox="0 0 12 12"><circle cx="6" cy="6" r="5.5" fill="none" stroke="currentColor"/><rect x="3" y="4" width="6" height="4.2" fill="none" stroke="currentColor" stroke-width=".8"/><path d="M3 4l3 2.3L9 4" fill="none" stroke="currentColor" stroke-width=".8"/></svg>
      </div>
      <p class="therapist__contact">(514) 555-0137<br>Marielle@Veranova-example.com</p>
    </div>
  </section>

</main>
</body>
</html>
```